Visual design for database driven web application

Need a clean, professional looking visual design for a web application.

PLUMB is the new standardized K-12 school testing program for the state of Texas. We are building an application named PLUMB-Finder (clever, yeah?) that will allow teachers, school administrators, and others to EASILY sort through millions of records of student data and print or export reports showing just the information they need about their students.

The state currently doesn't provide a user-friendly way to do this. They provide a "data dump" spreadsheet that school administrators and teachers must figure out how to manipulate to get the data they need. We are building a Web-based tool that will make it super simple and easy for our users to get the data they need in a format that works for them.

I've created a basic wireframe of the main application screen in Wirella Kit Plus. I need you to "skin" the wireframe to make it look good. Your mockup will set the tone for branding and visual design throughout the site.

See the attached screenshots. There are a few variations of the screen that include dynamic panels that open & close. Start by designing just the main screen and if you have time, do one or two of the panels. Thanks!
Updates

Target Market(s)

K-12 education professionals (teachers, administrators) in the state of Texas

Industry/Entity Type

Building

Requirements
Must have
• Your mockups should include all of the features & content shown in the attached screenshots.

However, you don't have to show all 10 rows of data. You can just do the column headers and one row of data. (It would be repetitive and unnecessary to spend time re-creating the entire grid with all of that data just to show your visual styling.)

The design should reflect the following concepts:

- Texas
- Education
- Simplicity
- Helpfulness
- Trust
- Professionalism

If I select your design, I will want your design source files (Illustrator, Photoshop, etc.)
Nice to have
• A logo in the upper left corner for PLUMB-Finder. The logo should definitely communicate the design concepts described under "must have."

```html
<!DOCTYPE html>
<html lang="en">
<head>
<meta charset="utf-8">
<title>PLUMB-Finder – Student Data</title>
<link rel="stylesheet" href="https://fonts.googleapis.com/css2?family=Noto+Sans:wght@400;700&display=swap">
<style>
  :root {
    --bg-top: #1ea2b6;
    --bg-bottom: #2cb8cf;
    --header: #1fa3b7;
    --rule: #a9d7e0;
    --ink: #0f2a30;
    --ink-soft: #e2f4f7;
    --brand: #eef8fa;
    --teal-text: #1e93aa;
    --tab-idle: #2997ab;
    --panel: #ffffff;
    --head-cell: #b5dee4;
    --grid-line: #d9e4e7;
    --pager: #a6e1ea;
    --btn-light: #e6f6f8;
    --search-field: #4cb8c7;
    --search-btn: #2ec4e2;
  }
  * { box-sizing: border-box; margin: 0; padding: 0; }
  html, body { width: 1200px; height: 803px; overflow: hidden; }
  body {
    position: relative;
    font-family: "Noto Sans", Verdana, sans-serif;
    background: linear-gradient(180deg, var(--bg-top) 0%, var(--bg-top) 20%, var(--bg-bottom) 100%);
    color: var(--ink);
  }
  .site-header { position: absolute; left: 0; top: 0; width: 1200px; height: 143px; background: var(--header); }
  .brand {
    position: absolute; left: 69px; top: 60px;
    font-weight: 700; font-size: 36px; color: var(--brand); letter-spacing: .5px;
  }
  .welcome { position: absolute; left: 594px; top: 32px; font-size: 14px; }
  .account-links { position: absolute; left: 810px; top: 33px; font-size: 12.5px; font-weight: 700; color: var(--ink-soft); letter-spacing: .8px; word-spacing: 4px; }
  .tools { position: absolute; left: 1062px; top: 24px; display: flex; gap: 10px; align-items: center; }
  .tools .sep { width: 1px; height: 20px; background: #7fcfdb; }
  .search { position: absolute; left: 811px; top: 73px; width: 254px; height: 31px; background: var(--search-field); border: 1px solid #2a7f8e; box-shadow: inset 0 1px 2px rgba(0,0,0,.25); }
  .search svg { position: absolute; right: 2px; top: 1px; }
  .search-btn { position: absolute; left: 1075px; top: 77px; width: 91px; height: 18px; background: var(--search-btn); border-radius: 3px; color: #fff; font-weight: 700; font-size: 14px; text-align: center; line-height: 18px; letter-spacing: .5px; }
  .search-option { position: absolute; left: 923px; top: 107px; font-size: 12.5px; color: var(--ink-soft); letter-spacing: .5px; display: flex; gap: 6px; align-items: center; }
  .rule { position: absolute; left: 0; top: 142px; width: 1200px; height: 7px; background: var(--rule); }
  .tab { position: absolute; top: 195px; height: 35px; width: 205px; text-align: center; line-height: 35px; font-size: 17px; color: var(--ink-soft); }
  .tab--active { left: 105px; background: linear-gradient(180deg, #19c7f2, #16b3da); }
  .tab--idle { left: 334px; background: var(--tab-idle); }
  .panel { position: absolute; left: 36px; top: 230px; width: 1132px; height: 452px; background: var(--panel); border-radius: 3px; overflow: hidden; }
  .data-grid { position: absolute; left: 14px; top: 23px; border-collapse: collapse; table-layout: fixed; width: 1104px; }
  .data-grid th { background: var(--head-cell); height: 34px; font-weight: 400; font-size: 14.5px; text-align: center; border-left: 2px solid #fff; }
  .data-grid th:first-child { border-left: 0; }
  .data-grid td { height: 38px; padding: 0; font-size: 14.5px; color: var(--teal-text); text-align: center; border-left: 1px solid var(--grid-line); border-bottom: 1px solid var(--grid-line); }
  .data-grid td:first-child { border-left: 0; }
  .data-grid tr:last-child td { border-bottom: 0; height: 46px; vertical-align: top; padding-top: 8px; }
  .pager { position: absolute; left: 37px; top: 694px; width: 1130px; height: 48px; background: var(--pager); border-radius: 3px; }
  .page-label { position: absolute; left: 44px; top: 14px; font-size: 14.5px; }
  .page-label .current { color: var(--ink); margin-left: 8px; }
  .page-label .rest { color: #6fb9c6; }
  .pager-btn { position: absolute; top: 14px; width: 109px; height: 26px; background: var(--btn-light); font-weight: 700; font-size: 14.5px; color: #3d6e76; text-align: center; line-height: 26px; letter-spacing: .5px; }
  .pager-btn--next { left: 269px; }
  .pager-btn--prev { left: 393px; }
  .show-label { position: absolute; left: 883px; top: 14px; font-weight: 700; font-size: 15px; color: #1a9bb4; letter-spacing: .5px; }
  .page-size { position: absolute; left: 944px; top: 8px; width: 85px; height: 32px; background: #bfe9ef; border-radius: 4px; font-weight: 700; font-size: 15px; line-height: 32px; padding-left: 18px; color: #2e5b62; }
  .page-size svg { position: absolute; right: 8px; top: 4px; }
</style>
</head>
<body>
  <header class="site-header">
    <div class="brand">PLUMB-Finder</div>
    <div class="welcome">Welcome &nbsp;: Jack</div>
    <div class="account-links">My Profile &nbsp;/ Logout</div>
    <div class="tools">
      <svg width="22" height="20" viewBox="0 0 22 20" aria-label="Print">
        <rect x="5" y="1" width="12" height="6" fill="#fff"/>
        <rect x="1" y="7" width="20" height="8" rx="1" fill="#cfe3e6"/>
        <rect x="3" y="9" width="16" height="2" fill="#7ac64a"/>
        <rect x="5" y="13" width="12" height="6" fill="#fff" stroke="#9bb" stroke-width=".5"/>
      </svg>
      <span class="sep"></span>
      <svg width="18" height="20" viewBox="0 0 18 20" aria-label="Export">
        <rect x="1" y="1" width="16" height="18" rx="1" fill="#2e3f44"/>
        <rect x="4" y="2" width="10" height="6" fill="#fff"/>
        <path d="M9 9v8M6 14l3 3 3-3" stroke="#e7c531" stroke-width="2" fill="none"/>
      </svg>
    </div>
    <div class="search">
      <svg width="36" height="28" viewBox="0 0 36 28" aria-label="Search">
        <circle cx="15" cy="12" r="8" fill="none" stroke="#1a4f58" stroke-width="3"/>
        <path d="M21 18l9 8" stroke="#1a4f58" stroke-width="4" stroke-linecap="round"/>
      </svg>
    </div>
    <div class="search-btn">Search</div>
    <div class="search-option">Search&nbsp; Option
      <svg width="24" height="14" viewBox="0 0 24 14"><path d="M1 1h22L12 13z" fill="none" stroke="#e2f4f7" stroke-width="1.3"/></svg>
    </div>
  </header>
  <div class="rule"></div>

  <div class="tab tab--active">Instructions</div>
  <div class="tab tab--idle">Student Data</div>

  <main class="panel">
    <table class="data-grid">
      <colgroup>
        <col style="width:67px"><col style="width:67px"><col style="width:61px"><col style="width:118px">
        <col style="width:86px"><col style="width:121px"><col style="width:108px"><col style="width:119px">
        <col style="width:43px"><col style="width:124px"><col style="width:71px"><col style="width:119px">
      </colgroup>
      <thead>
        <tr><th>Date</th><th>Grade</th><th>ESC</th><th>CDC#</th><th>District</th><th>Campus</th><th>Last Name</th><th>First Name</th><th>MI</th><th>Student ID</th><th>Gender</th><th>DOB</th></tr>
      </thead>
      <tbody>
        <tr><td>411</td><td>9</td><td>10</td><td>9999999999</td><td>Example</td><td>Examble H S</td><td>Alvorado</td><td>NATHALE</td><td>I</td><td>1234546734</td><td>F</td><td>28/03/1980</td></tr>
        <tr><td>411</td><td>9</td><td>10</td><td>9999999999</td><td>Example</td><td>Examble H S</td><td>Alvorado</td><td>NATHALE</td><td>I</td><td>1234546734</td><td>F</td><td>28/03/1980</td></tr>
        <tr><td>411</td><td>9</td><td>10</td><td>9999999999</td><td>Example</td><td>Examble H S</td><td>Alvorado</td><td>NATHALE</td><td>I</td><td>1234546734</td><td>F</td><td>28/03/1980</td></tr>
        <tr><td>411</td><td>9</td><td>10</td><td>9999999999</td><td>Example</td><td>Examble H S</td><td>Alvorado</td><td>NATHALE</td><td>I</td><td>1234546734</td><td>F</td><td>28/03/1980</td></tr>
        <tr><td>411</td><td>9</td><td>10</td><td>9999999999</td><td>Example</td><td>Examble H S</td><td>Alvorado</td><td>NATHALE</td><td>I</td><td>1234546734</td><td>F</td><td>28/03/1980</td></tr>
        <tr><td>411</td><td>9</td><td>10</td><td>9999999999</td><td>Example</td><td>Examble H S</td><td>Alvorado</td><td>NATHALE</td><td>I</td><td>1234546734</td><td><b>F</b></td><td><b>28/03/1980</b></td></tr>
        <tr><td>411</td><td>9</td><td>10</td><td>9999999999</td><td>Example</td><td>Examble H S</td><td>Alvorado</td><td>NATHALE</td><td>I</td><td>1234546734</td><td>F</td><td>28/03/1980</td></tr>
        <tr><td>411</td><td>9</td><td>10</td><td>9999999999</td><td>Example</td><td>Examble H S</td><td>Alvorado</td><td>NATHALE</td><td>I</td><td>1234546734</td><td>F</td><td>28/03/1980</td></tr>
        <tr><td>411</td><td>9</td><td>10</td><td>9999999999</td><td>Example</td><td>Examble H S</td><td>Alvorado</td><td>NATHALE</td><td>I</td><td>1234546734</td><td>F</td><td>28/03/1980</td></tr>
        <tr><td>411</td><td>9</td><td>10</td><td>9999999999</td><td>Example</td><td>Examble H S</td><td>Alvorado</td><td>NATHALE</td><td>I</td><td>1234546734</td><td>F</td><td>28/03/1980</td></tr>
      </tbody>
    </table>
  </main>

  <nav class="pager">
    <div class="page-label">Page : <span class="current">1</span> <span class="rest">2 3 4.......25</span></div>
    <div class="pager-btn pager-btn--next">Next</div>
    <div class="pager-btn pager-btn--prev">Previous</div>
    <div class="show-label">Show</div>
    <div class="page-size">10
      <svg width="22" height="24" viewBox="0 0 22 24"><path d="M2 10L11 2l9 8zM2 14l9 8 9-8z" fill="#4a6f75"/></svg>
    </div>
  </nav>
</body>
</html>
```